Psychologist in Private Practice Needs a Website Update

Project Description:
Hello talented designers! My current website, www.jodelbrisk.com, needs a fresh, boho-modern makeover that highlights the warm, welcoming nature of my holistic therapy practice. I want a website that has a serene, boho- modern design, appealing to clients seeking individual therapy, couples therapy, and family counseling.

I’d also like to prepare for a future second site focused exclusively on couples and family therapy. Both sites should be interconnected, so I’m looking for design suggestions that seamlessly link them together while maintaining a cohesive brand look and feel.

Key Objectives:

Boho-Modern Aesthetic: Incorporate natural textures, neutral or earthy tones, and clean lines that capture a modern, inviting vibe.

Responsive Design: Ensure the website is user-friendly on desktop, tablet, and mobile devices.

Clear Service Offerings: Prominently feature my three distinct services: individual therapy, couples therapy, and family counseling.

Interlinked Future Site: Provide ideas on how to cross-link this site with a second site focused on couples and family therapy.

User Experience (UX): Make the site simple to navigate, with intuitive placement of content that speaks to potential clients’ needs.

SEO-Friendly: Implement best practices for structure, site speed, and keyword usage to boost online visibility.

What I Have Now:
Existing website: www.jodelbrisk.com
Basic content and a logo that can be refined or updated to match the boho-modern feel
Rough style guide with brand elements open to a fresh interpretation

Preferred Style/Tone:
Boho-modern with earthy tones, subtle textures, and clean typography
Warm, empathetic, and approachable to align with the nature of therapy services
Slightly artistic or organic elements that evoke calm and connection

Potential for an ongoing design relationship!
Updates

Need extra days to review

Target Market(s)

I have a high functioning, professional clientele who doctors, lawyers, and leaders in their field.

Industry/Entity Type

healthcare/mental health

Coding

Coded - Design and coding required

Font styles to use
Other font styles liked:
• cormorant garamond for headers and Source Sans Pro for supporting text

Colors

Designer to choose colors to be used in the design.

Requirements
Must have
• Open, Harmonious Layout I’d like the overall design to feel upscale, humanistic, open and harmonious, with minimal divisions of space. Rather than traditional section dividers, please consider using images, subtle shifts in color, typography, or spacing to define sections. Hero Image & Inspiration Ideally, the first (hero) image should evoke a sense of awe or inspiration. Focus on simplicity and elegance so the design feels spacious and inviting, allowing the content and imagery to really stand out. Natural Flow Wherever possible, let the design elements flow naturally into each other, creating a sense of unity and cohesion throughout the site.
Nice to have
• 1. Full-Width Hero Image: • The homepage should feature a full-width hero image that extends edge-to-edge across the screen for a modern and visually immersive effect. • This image should set the tone for the website, reflecting a calming, humanistic/natural, and upscale feel. It could include subtle overlays or gradients to enhance readability of text and navigation elements. Ideally, this image should have one or two people in nature. The image could be slightly transparent to allow the text "holistic therapy" and the tagline "an integrative approach to transformation" to be easily visible. Please help me find a breath-taking image that evokes a sense of beauty, inspiration, awe or hope. 2. Menu Tabs Positioned Over the Image: • The menu tabs (navigation bar) should be positioned directly on top of the hero image, either centered or aligned to the top right/left, depending on the design. • The navigation bar should have a slightly transparent or solid background (depending on the image and visibility needs) to ensure the text is easily readable without detracting from the image. 3. Typography and Text Placement: • The text overlay on the hero image should use the selected fonts: • Cormorant Garamond for headers (e.g., the tagline or welcome message). • Source Sans Pro for any supporting text. 5. Seamless Transitions: • Below the full-width image, transitions into the next sections (like “About,” “Services,” or client-focused content) should be smooth, using full-width separators that maintain the cohesive, open layout style. 6. Color Palette: • A neutral and calming color palette should be used (e.g., soft blues, grays, whites, or very muted earth tones) to create a soothing atmosphere for visitors. This design approach ensures the homepage looks clean, modern, and professional while maintaining the calming and upscale aesthetic that reflects the values of my psychology practice

```html
<!DOCTYPE html>
<html lang="en">
<head>
<meta charset="utf-8">
<title>Dr. Lena Marsh – Holistic Therapy</title>
<link rel="stylesheet" href="https://fonts.googleapis.com/css2?family=Marcellus&family=Source+Sans+3:wght@400;600&display=swap">
<style>
:root{
  --plum:#7b2f66;
  --plum-deep:#6a3257;
  --plum-dark:#3f2233;
  --ink:#3b1f33;
  --body:#4a4048;
  --peach:#fdf3ec;
  --blush:#f8e4e2;
  --gold:#e2b866;
  --white:#ffffff;
  --line:#e4dbe0;
}
*{box-sizing:border-box;margin:0;padding:0}
html,body{width:1200px;height:4295px;overflow:hidden}
body{position:relative;background:var(--white);font-family:"Source Sans 3",Arial,sans-serif;color:var(--body)}
.abs{position:absolute}
.serif{font-family:"Marcellus",Georgia,serif;font-weight:400}
.label{font-size:11px;letter-spacing:2.2px;color:var(--plum);font-weight:600}
.h2{font-family:"Marcellus",Georgia,serif;font-weight:400;font-size:35px;line-height:1.22;color:var(--ink)}
.center{left:0;width:1200px;text-align:center}
.btn{position:absolute;display:flex;align-items:center;gap:14px;height:37px;border-radius:19px;padding:0 22px 0 5px;font-size:12px;font-weight:600;text-decoration:none}
.btn .dot{width:27px;height:27px;border-radius:50%;display:flex;align-items:center;justify-content:center}
.btn-light{background:var(--white);color:var(--plum)}
.btn-light .dot{background:var(--plum)}
.btn-dark{background:var(--plum);color:var(--white)}
.btn-dark .dot{background:var(--white)}
.logo{font-family:"Source Sans 3",Arial,sans-serif;font-size:22px;line-height:1.05;color:var(--ink)}
.logo small{display:block;font-size:17px}

/* header & hero */
.hero-band{left:0;top:0;width:1200px;height:508px;background:var(--peach)}
.nav{top:36px;left:488px;display:flex;gap:24px;font-size:12px;color:var(--ink)}
.nav .active{color:var(--plum)}
.hero{left:32px;top:87px;width:1136px;height:500px;border-radius:20px;overflow:hidden;
  background:linear-gradient(180deg,#e9a05c 0%,#f08a3e 25%,#c85a2f 50%,#8d3a2a 75%,#4a2020 100%)}
.hero-title{top:288px;left:0;width:100%;text-align:center;font-size:52px;color:var(--white)}
.hero-sub{top:360px;left:0;width:100%;text-align:center;font-family:"Marcellus",Georgia,serif;font-size:19px;color:#fbefe4;letter-spacing:.4px}

/* about */
.about p,.about li{font-size:11px;line-height:1.6;color:var(--body)}
.about ul{list-style:none}
.about li{display:flex;align-items:center;gap:12px;margin-bottom:4.6px}
.photo{border-radius:10px}

/* values */
.values{left:0;top:1300px;width:1200px;height:555px;background:radial-gradient(ellipse at 20% 30%,#fbe0dc 0%,#fdf1ee 45%,#f9e2e0 100%)}
.value{position:absolute;width:230px;background:var(--white);border-radius:115px;text-align:center;padding:0 30px;box-shadow:0 4px 18px rgba(160,90,110,.08)}
.value h3{font-family:"Marcellus",Georgia,serif;font-weight:400;font-size:23px;color:var(--plum);margin:10px 0 10px}
.value p{font-size:11px;line-height:1.6;color:var(--body)}
.value svg{margin-top:60px}

/* services */
.services{left:0;top:1855px;width:1200px;height:540px;background:var(--plum-deep)}
.svc{position:absolute;top:203px;width:314px;height:217px;border-radius:8px;overflow:hidden;background:linear-gradient(160deg,#d9d2c8 0%,#a59a8c 55%,#3c2b2a 100%)}
.svc span{position:absolute;left:20px;bottom:20px;font-family:"Marcellus",Georgia,serif;font-size:22px;color:var(--white)}

/* faq */
.faq-q{position:absolute;left:613px;width:479px;display:flex;align-items:center;gap:14px;font-size:14px;color:var(--plum)}
.faq-num{width:30px;height:30px;border-radius:50%;background:#efe9ed;display:flex;align-items:center;justify-content:center;font-size:10px;color:var(--ink)}
.faq-num.open{background:var(--plum);color:var(--white)}
.faq-sign{margin-left:auto;font-size:22px;color:var(--ink);font-weight:400}
.faq-line{position:absolute;left:613px;width:479px;height:1px;background:var(--line)}
.faq-ans{left:656px;top:2490px;width:436px;font-size:10.5px;line-height:1.55;color:var(--body)}
.faq-ans p+p{margin-top:8px}

/* blog */
.blog-band{left:0;top:2853px;width:1200px;height:905px;background:linear-gradient(180deg,#fff6ef 0%,#fdeee4 100%)}
.post-img{position:absolute;width:314px;border-radius:8px}
.post-date{position:absolute;font-size:11px;color:var(--body)}
.post-title{position:absolute;width:320px;font-family:"Marcellus",Georgia,serif;font-size:24px;line-height:1.15;color:var(--ink)}
.read{position:absolute;font-size:11px;font-weight:600;color:var(--plum);display:flex;align-items:center;gap:6px}

/* cta & footer */
.foot{left:0;top:3758px;width:1200px;height:537px;background:var(--plum-dark)}
.cta{left:32px;top:3702px;width:1136px;height:373px;border-radius:20px;background:linear-gradient(100deg,#6e3455 0%,#7e4058 45%,#b06e5e 75%,#c88c6a 100%)}
.cta p{font-size:11.5px;line-height:1.6;color:#f6e7ee}
.fnav{top:4157px;left:428px;display:flex;gap:26px;font-size:11px;color:var(--white)}
</style>
</head>
<body>

<!-- Header -->
<div class="abs hero-band"></div>
<div class="abs logo" style="left:42px;top:20px">Dr. Lena Marsh<small>Licensed Psychologist</small></div>
<nav class="abs nav">
  <span class="active">Home</span><span>About</span>
  <span>Services <svg width="8" height="6" viewBox="0 0 8 6"><path d="M1 1.5 4 4.5 7 1.5" fill="none" stroke="#3b1f33" stroke-width="1.2"/></svg></span>
  <span>Blog</span><span>FAQs</span>
</nav>
<a class="btn btn-dark" style="left:1035px;top:25px;height:36px">
  <span class="dot"><svg width="11" height="8" viewBox="0 0 11 8"><path d="M0 4h9M6 1l3 3-3 3" fill="none" stroke="#7b2f66" stroke-width="1.3"/></svg></span>Contact Us</a>

<!-- Hero -->
<section class="abs hero" role="img" aria-label="Golden sunset over rolling mountain ridges">
  <h1 class="abs hero-title serif">Holistic Therapy</h1>
  <p class="abs hero-sub">An interactive approach to transformtion</p>
</section>
<a class="btn btn-light" style="left:522px;top:500px;width:155px">
  <span class="dot"><svg width="11" height="8" viewBox="0 0 11 8"><path d="M0 4h9M6 1l3 3-3 3" fill="none" stroke="#fff" stroke-width="1.3"/></svg></span>Book a Session</a>

<!-- About -->
<section class="about">
  <div class="abs label" style="left:110px;top:637px">ABOUT US</div>
  <h2 class="abs h2" style="left:110px;top:666px;width:470px;line-height:1.2">Are you struggling with issues that affect the way you live, love or work?</h2>
  <p class="abs" style="left:110px;top:820px;width:480px">Dr. Lena Marsh and her associates are licensed psychologists in Fernbrook, Maryland. We offer therapy for individuals, couples and families to help you create meaningful change, whether you:</p>
  <ul class="abs" style="left:110px;top:882px;width:480px">
    <li><svg width="14" height="10" viewBox="0 0 14 10"><path d="M7 9C4 7 1 6 1 3c2 0 4 1 6 4 2-3 4-4 6-4 0 3-3 4-6 6Z" fill="#7b2f66"/></svg>Feel overwhelmed with depression or anxiety.</li>
    <li><svg width="14" height="10" viewBox="0 0 14 10"><path d="M7 9C4 7 1 6 1 3c2 0 4 1 6 4 2-3 4-4 6-4 0 3-3 4-6 6Z" fill="#7b2f66"/></svg>Experience a lack of connection in your marriage.</li>
    <li><svg width="14" height="10" viewBox="0 0 14 10"><path d="M7 9C4 7 1 6 1 3c2 0 4 1 6 4 2-3 4-4 6-4 0 3-3 4-6 6Z" fill="#7b2f66"/></svg>Worry excessively about what others think.</li>
    <li><svg width="14" height="10" viewBox="0 0 14 10"><path d="M7 9C4 7 1 6 1 3c2 0 4 1 6 4 2-3 4-4 6-4 0 3-3 4-6 6Z" fill="#7b2f66"/></svg>Have a history of trauma or abuse.</li>
    <li><svg width="14" height="10" viewBox="0 0 14 10"><path d="M7 9C4 7 1 6 1 3c2 0 4 1 6 4 2-3 4-4 6-4 0 3-3 4-6 6Z" fill="#7b2f66"/></svg>Parent a child with complex needs.</li>
    <li><svg width="14" height="10" viewBox="0 0 14 10"><path d="M7 9C4 7 1 6 1 3c2 0 4 1 6 4 2-3 4-4 6-4 0 3-3 4-6 6Z" fill="#7b2f66"/></svg>Struggle with other life challenges</li>
  </ul>
  <div class="abs photo" style="left:110px;top:1030px;width:480px;height:218px;background:linear-gradient(90deg,#6a3a22 0%,#b47a45 40%,#e6d8c4 70%,#8a7a64 100%)" role="img" aria-label="Warm office hallway with french doors and a waiting area"></div>
  <div class="abs photo" style="left:693px;top:638px;width:399px;height:404px;background:radial-gradient(ellipse at 50% 40%,#c99a74 0%,#8e6a4e 40%,#4a3a30 100%)" role="img" aria-label="Portrait of the psychologist"></div>
  <p class="abs" style="left:693px;top:1063px;width:399px">We have extensive experience treating a full spectrum of mental health disorders using a collaborative and compassionate approach. In addition to individual therapy, we also provide couples counseling and family therapy.</p>
  <p class="abs" style="left:693px;top:1123px;width:399px">Dr. Marsh's practice, based in the West Fernbrook area of Ashford, is best suited for those who wish to deeply examine their inner world to gain insight, identify what matters most, and create lasting change towards a more fulfilling life.</p>
  <a class="btn btn-dark" style="left:693px;top:1212px;width:135px">
    <span class="dot"><svg width="11" height="8" viewBox="0 0 11 8"><path d="M0 4h9M6 1l3 3-3 3" fill="none" stroke="#7b2f66" stroke-width="1.3"/></svg></span>Learn More</a>
</section>

<!-- Values -->
<section class="abs values">
  <div class="abs label center" style="top:53px">Our Values</div>
  <h2 class="abs h2 center" style="top:78px">The Values We Cherish at<br>Quiet Grove</h2>
  <div class="value" style="left:110px;top:183px;height:292px">
    <svg width="44" height="44" viewBox="0 0 44 44" fill="none" stroke="#7b2f66" stroke-width="1.4"><path d="M22 16c-3-4-9-1-6 4l6 6 6-6c3-5-3-8-6-4Z"/><path d="M8 8c0 10 4 18 10 24M36 8c0 10-4 18-10 24"/></svg>
    <h3>Compassion</h3><p>We create a warm, supportive space where every individual feels seen, heard, and valued on their healing journey.</p></div>
  <div class="value" style="left:360px;top:183px;height:322px">
    <svg width="44" height="44" viewBox="0 0 44 44" fill="none" stroke="#7b2f66" stroke-width="1.4"><circle cx="22" cy="22" r="4"/><path d="M22 4c5 6 5 10 0 14-5-4-5-8 0-14ZM22 40c5-6 5-10 0-14-5 4-5 8 0 14ZM4 22c6-5 10-5 14 0-4 5-8 5-14 0ZM40 22c-6-5-10-5-14 0 4 5 8 5 14 0Z"/></svg>
    <h3>Integrity</h3><p>We uphold honesty and transparency, ensuring that all interactions are based on trust and respect.</p></div>
  <div class="value" style="left:610px;top:183px;height:292px">
    <svg width="44" height="44" viewBox="0 0 44 44" fill="none" stroke="#7b2f66" stroke-width="1.4"><ellipse cx="22" cy="9" rx="7" ry="4"/><ellipse cx="22" cy="20" rx="10" ry="5"/><ellipse cx="22" cy="33" rx="13" ry="6"/></svg>
    <h3>Growth</h3><p>We believe in continuous growth, encouraging personal self-discovery, and transformation for everyone we serve.</p></div>
  <div class="value" style="left:860px;top:183px;height:322px">
    <svg width="44" height="44" viewBox="0 0 44 44" fill="none" stroke="#7b2f66" stroke-width="1.4"><path d="M14 40V24l-2-6 4-2 2 6V12h4v10-12h4v12-9h4v12l2-5h3l-3 12c-1 4-3 6-6 6Z"/><path d="M20 4v3M26 3v3M32 6l-2 2"/></svg>
    <h3>Empowerment</h3><p>We uphold honesty and transparency, ensuring that all interactions are based on trust and respect.</p></div>
</section>

<!-- Services -->
<section class="abs services">
  <div class="abs label center" style="top:57px;color:var(--gold)">Our Services</div>
  <h2 class="abs h2 center" style="top:100px;color:var(--white)">Your Journey to Inner Peace<br>and Transformation</h2>
  <div class="svc" style="left:110px" role="img" aria-label="Therapist in session with a client"><span>Individual Therapy</span></div>
  <div class="svc" style="left:443px" role="img" aria-label="Couple speaking with a counselor"><span>Couples Therapy</span></div>
  <div class="svc" style="left:777px" role="img" aria-label="Family in a counseling session"><span>Family Therapy</span></div>
  <a class="btn btn-light" style="left:522px;top:452px;width:155px">
    <span class="dot"><svg width="11" height="8" viewBox="0 0 11 8"><path d="M0 4h9M6 1l3 3-3 3" fill="none" stroke="#fff" stroke-width="1.3"/></svg></span>Book a Session</a>
</section>

<!-- FAQ -->
<section class="faq">
  <div class="abs label" style="left:110px;top:2445px">Frequently Answered Questions</div>
  <h2 class="abs h2" style="left:110px;top:2472px;width:450px">Everything You Need to Know About Our Holistic Therapy Services</h2>
  <a class="btn btn-dark" style="left:110px;top:2634px;width:118px">
    <span class="dot"><svg width="11" height="8" viewBox="0 0 11 8"><path d="M0 4h9M6 1l3 3-3 3" fill="none" stroke="#7b2f66" stroke-width="1.3"/></svg></span>View All</a>

  <div class="faq-q" style="top:2444px"><span class="faq-num open">01</span>Where are you located?<span class="faq-sign">–</span></div>
  <div class="abs faq-ans">
    <p>Our clinicians hold both virtual and in person sessions.Virtual sessions are held via Calmlink.</p>
    <p>In person sessions are held out of our office location at 418 Willowmere Lane, Fernbrook MD 20999. The home office has a separate entrance. You should walk up the front walkway toward the porch, bear left and follow the path along the side of the house. Just before you reach the gate, you will see stairs leading down to the waiting room entrance.</p>
  </div>
  <div class="faq-line" style="top:2620px"></div>
  <div class="faq-q" style="top:2635px"><span class="faq-num">02</span>What states do you offer telehealth in?<span class="faq-sign">+</span></div>
  <div class="faq-line" style="top:2682px"></div>
  <div class="faq-q" style="top:2697px"><span class="faq-num">03</span>What types of clients do you see?<span class="faq-sign">+</span></div>
  <div class="faq-line" style="top:2743px"></div>
  <div class="faq-q" style="top:2758px"><span class="faq-num">04</span>Do you take insurance?<span class="faq-sign">+</span></div>
  <div class="faq-line" style="top:2805px"></div>
</section>

<!-- Blog -->
<section>
  <div class="abs blog-band"></div>
  <div class="abs label center" style="top:2905px">Latest Blogs</div>
  <h2 class="abs h2 center" style="top:2935px">Dive Deeper into Healing<br>and Growth</h2>

  <div class="post-img" style="left:110px;top:3055px;height:262px;background:linear-gradient(180deg,#d9a86a 0%,#b98450 50%,#8a6a3e 100%)" role="img" aria-label="Woman with open arms in a golden field"></div>
  <div class="post-date" style="left:110px;top:3340px">Jan 09, 2025</div>
  <div class="post-title" style="left:110px;top:3362px">Empowering Self-Healing Practices</div>
  <div class="read" style="left:110px;top:3432px">Read More <svg width="12" height="8" viewBox="0 0 12 8"><path d="M0 4h10M7 1l3 3-3 3" fill="none" stroke="#7b2f66" stroke-width="1.2"/></svg></div>

  <div class="post-img" style="left:443px;top:3055px;height:348px;background:linear-gradient(180deg,#ecebe8 0%,#c9c2b8 50%,#6d5a6a 100%)" role="img" aria-label="Counselor taking notes while talking with a young man"></div>
  <div class="post-date" style="left:443px;top:3428px">Jan 09, 2025</div>
  <div class="post-title" style="left:443px;top:3450px">Manifesting with Intention Workshop</div>
  <div class="read" style="left:443px;top:3519px">Read More <svg width="12" height="8" viewBox="0 0 12 8"><path d="M0 4h10M7 1l3 3-3 3" fill="none" stroke="#7b2f66" stroke-width="1.2"/></svg></div>

  <div class="post-img" style="left:776px;top:3055px;height:305px;background:linear-gradient(180deg,#2f5a5c 0%,#3e6a68 50%,#6b5a5a 100%)" role="img" aria-label="Two women meditating in a calm room"></div>
  <div class="post-date" style="left:776px;top:3385px">Jan 09, 2025</div>
  <div class="post-title" style="left:776px;top:3405px;width:340px">Chakra Balancing Workshop</div>
  <div class="read" style="left:776px;top:3447px">Read More <svg width="12" height="8" viewBox="0 0 12 8"><path d="M0 4h10M7 1l3 3-3 3" fill="none" stroke="#7b2f66" stroke-width="1.2"/></svg></div>

  <a class="btn btn-dark" style="left:507px;top:3564px;width:153px">
    <span class="dot"><svg width="11" height="8" viewBox="0 0 11 8"><path d="M0 4h9M6 1l3 3-3 3" fill="none" stroke="#7b2f66" stroke-width="1.3"/></svg></span>Read All Blogs</a>
</section>

<!-- CTA & Footer -->
<footer>
  <div class="abs foot"></div>
  <div class="abs cta" role="img" aria-label="Woman in profile with eyes closed in warm sunlight">
    <div class="abs label" style="left:50px;top:75px;color:var(--gold)">Let's Connect</div>
    <h2 class="abs h2" style="left:50px;top:102px;color:var(--white)">Therapy is a Partnership</h2>
    <p class="abs" style="left:50px;top:167px;width:490px">Our clinicians utilize contemporary neuroscience-informed therapies along with the wisdom of traditional psychotherapy to foster insight, mindfulness, self-compassion, and deeper connections to oneself and others. Together, in a safe and non-judgmental environment, we will work to understand what holds you back from living the life you really want. All are welcome and celebrated.</p>
  </div>
  <a class="btn btn-light" style="left:82px;top:3965px;width:133px">
    <span class="dot"><svg width="11" height="8" viewBox="0 0 11 8"><path d="M0 4h9M6 1l3 3-3 3" fill="none" stroke="#fff" stroke-width="1.3"/></svg></span>Contact Us</a>

  <div class="abs logo" style="left:42px;top:4147px;color:var(--white)">Dr. Lena Marsh<small>Licensed Psychologist</small></div>
  <nav class="abs fnav"><span>Home</span><span>About</span><span>Services</span><span>Blog</span><span>FAQs</span><span>Contact Us</span></nav>
  <div class="abs" style="right:32px;top:4135px;text-align:right;color:var(--white)">
    <div style="font-size:14px;text-decoration:underline">drlenamarsh@mailbox.com</div>
    <div style="font-size:23px;margin-top:8px">(555) 214-0387</div>
  </div>
  <div class="abs center" style="top:4262px;font-size:10.5px;color:#d9c8d2">© 2022 Lena R. Marsh, Psy.D.</div>
</footer>

</body>
</html>
```